DRIFTFRAME studio

Design to be modern with colours of logo, maybe orange background. Include name, position, phone/WhatsApp email/web. Specialises in long form TIMELAPSE

Contact Information for Business Card

Marcus Ellery, filmmaker,/photographer, phone/WhatsApp +971528306457, email - marcus@driftframestudio.example www.driftframestudio.example, instagram @driftframestudio

Font styles to use
Sans Serif

Requirements
Must have
• Fresh, bright, modern, original
Marcus Ellery - Filmmaker/Photographer
Phone/WhatsApp +971 528 30 6457
email - marcus@driftfarmestudio.example
Web - driftfarmestudio.example
PoBox 584193, Dubai, UAE
instagram - driftframestudio
Should not have
• solid black background

```html
<!DOCTYPE html>
<html lang="en">
<head>
<meta charset="UTF-8">
<title>DRIFTFRAME studio – Business Card</title>
<link rel="stylesheet" href="https://fonts.googleapis.com/css2?family=Arimo:wght@400;700&display=swap">
<style>
  :root {
    --brand-orange: #f37421;
    --ink: #111111;
    --paper: #ffffff;
    --backdrop: #ecebe8;
    --card-w: 620px;
    --card-h: 354px;
  }
  * { margin: 0; padding: 0; box-sizing: border-box; }
  html, body {
    width: 1200px; height: 900px; overflow: hidden;
    background: var(--backdrop);
    font-family: "Arimo", Arial, sans-serif;
  }
  .card-sheet {
    width: 1200px; height: 900px;
    display: flex; flex-direction: column;
    align-items: center; justify-content: center; gap: 48px;
  }
  .card {
    position: relative;
    width: var(--card-w); height: var(--card-h);
    overflow: hidden;
    box-shadow: 0 6px 18px rgba(0,0,0,0.18);
  }
  /* Front */
  .card--front {
    background: var(--brand-orange);
    display: flex; align-items: center; justify-content: center;
  }
  .brand-mark {
    display: flex; align-items: center; gap: 14px;
  }
  .brand-mark__dot {
    width: 46px; height: 46px; border-radius: 50%;
    border: 4px solid currentColor;
  }
  .brand-mark__name {
    font-weight: 700; text-transform: uppercase;
    line-height: 0.95; letter-spacing: 0.5px;
  }
  .card--front .brand-mark { color: var(--paper); }
  .card--front .brand-mark__name { font-size: 34px; }

  /* Back */
  .card--back { background: var(--paper); }
  .card__waves {
    position: absolute; inset: 0; width: 100%; height: 100%;
  }
  .holder { position: absolute; left: 42px; top: 62px; }
  .holder__name {
    color: var(--brand-orange); font-weight: 700;
    font-size: 22px; text-transform: uppercase; letter-spacing: 0.3px;
  }
  .holder__role { color: var(--ink); font-size: 15px; margin-top: 4px; margin-left: 4px; }

  .card--back .brand-mark {
    position: absolute; right: 40px; top: 72px;
    color: var(--brand-orange); gap: 10px;
  }
  .card--back .brand-mark__dot { width: 34px; height: 34px; border-width: 3px; }
  .card--back .brand-mark__name { font-size: 21px; }

  .contact-list {
    position: absolute; left: 58px; top: 200px;
    list-style: none; font-size: 15px; color: var(--ink);
  }
  .contact-list li {
    display: flex; align-items: center; gap: 8px; height: 22px;
  }
  .contact-list svg { width: 17px; height: 17px; flex: none; }
  .accent { color: var(--brand-orange); }

  .social {
    position: absolute; right: 40px; top: 246px;
    display: flex; align-items: center; gap: 7px;
    color: var(--paper); font-size: 14px;
  }
  .social__dot {
    width: 15px; height: 15px; border-radius: 50%;
    border: 2px solid var(--paper);
  }
</style>
</head>
<body>
<main class="card-sheet">

  <section class="card card--front" aria-label="Business card front">
    <div class="brand-mark">
      <span class="brand-mark__dot"></span>
      <span class="brand-mark__name">Driftframe<br>Studio</span>
    </div>
  </section>

  <section class="card card--back" aria-label="Business card back">
    <svg class="card__waves" viewBox="0 0 620 354" preserveAspectRatio="none" aria-hidden="true">
      <path d="M0,304 C170,340 330,292 440,222 C510,178 565,158 620,150 L620,354 L0,354 Z" fill="#111111"/>
      <path d="M0,326 C170,354 335,302 445,230 C515,184 568,162 620,154 L620,354 L0,354 Z" fill="#f37421"/>
    </svg>

    <div class="holder">
      <h1 class="holder__name">Marcus Ellery</h1>
      <p class="holder__role">Filmmaker/Photographer</p>
    </div>

    <div class="brand-mark">
      <span class="brand-mark__dot"></span>
      <span class="brand-mark__name">Driftframe<br>Studio</span>
    </div>

    <ul class="contact-list">
      <li>
        <svg viewBox="0 0 20 20"><circle cx="10" cy="10" r="9" fill="#f37421"/><path d="M7 5.5l1.6 0 .8 2.3-1 .9c.6 1.3 1.5 2.2 2.8 2.8l.9-1 2.3.8 0 1.6c0 .6-.5 1-1.1 1-4.2-.3-7.3-3.4-7.5-7.4 0-.6.4-1 1.2-1z" fill="#fff"/></svg>
        <span>+971528306457</span>
      </li>
      <li>
        <svg viewBox="0 0 20 20"><rect x="1" y="4" width="18" height="12" rx="1" fill="#f37421"/><path d="M1.5 4.8 10 11l8.5-6.2" fill="none" stroke="#fff" stroke-width="1.4"/></svg>
        <span>marcus@<span class="accent">driftframestudio</span>.example</span>
      </li>
      <li>
        <svg viewBox="0 0 20 20"><circle cx="10" cy="10" r="9" fill="#f37421"/><g fill="none" stroke="#fff" stroke-width="1.2"><ellipse cx="10" cy="10" rx="3.6" ry="8"/><path d="M2 10h16M3.5 6h13M3.5 14h13"/></g></svg>
        <span>www.<span class="accent">driftframestudio</span>.example</span>
      </li>
    </ul>

    <div class="social">
      <span class="social__dot"></span>
      <span>@driftframestudio</span>
    </div>
  </section>

</main>
</body>
</html>
```